Business Card Design for Brightkeel

The company provides engineering tender consulting services and personnel resources. The target market is large engineering construction and services companies. The business is based in Australia.

```html
<!DOCTYPE html>
<html lang="en">
<head>
<meta charset="utf-8">
<title>Brightkeel — Business Card</title>
<link rel="stylesheet" href="https://fonts.googleapis.com/css2?family=Arimo:wght@400;700&family=Michroma&display=swap">
<style>
  :root {
    --page: #ffffff;
    --card: #ffffff;
    --card-edge: #8f8f8f;
    --ink: #111111;
    --ink-soft: #2a2a2a;
    --on-dark: #ffffff;
    --panel: #151515;
    --panel-rule: #9c9c9c;
    --accent: #e1251b;
    --rule: #9a9a9a;
    --ghost: #ececec;
    --back-panel: #f3f3f3;
  }
  * { margin: 0; padding: 0; box-sizing: border-box; }
  html, body { width: 1200px; height: 983px; overflow: hidden; background: var(--page); }
  body { position: relative; font-family: "Arimo", Arial, sans-serif; color: var(--ink); }

  .card {
    position: absolute;
    left: 241px;
    width: 666px;
    height: 403px;
    background: var(--card);
    border: 1px solid var(--card-edge);
    overflow: hidden;
  }
  .card--front { top: 60px; }
  .card--back { top: 481px; }

  /* Front */
  .brand {
    position: absolute;
    right: 296px;
    top: 60px;
    font-family: "Michroma", "Arimo", sans-serif;
    font-size: 26px;
    letter-spacing: 1px;
    color: var(--ink);
    line-height: 1;
  }
  .brand__square {
    position: absolute;
    left: 380px;
    top: 47px;
    width: 48px;
    height: 48px;
    background: var(--ink-soft);
  }
  .holder {
    position: absolute;
    right: 30px;
    top: 174px;
    text-align: right;
  }
  .holder__name { font-size: 16px; font-weight: 700; color: var(--ink); line-height: 1.2; }
  .holder__role { font-size: 12px; font-weight: 700; color: var(--ink-soft); line-height: 1.3; }

  .contact-panel {
    position: absolute;
    left: 0;
    right: 0;
    bottom: 0;
    height: 136px;
    background: var(--panel);
    border-top: 6px solid var(--panel-rule);
  }
  .contact {
    position: absolute;
    left: 36px;
    top: 280px;
    list-style: none;
    color: var(--on-dark);
    font-size: 15px;
    font-weight: 700;
    line-height: 20px;
  }

  /* Back */
  .back-panel {
    position: absolute;
    left: 0;
    right: 0;
    bottom: 0;
    height: 60px;
    background: var(--back-panel);
  }
  .ghost-brand {
    position: absolute;
    left: 28px;
    top: 52px;
    font-family: "Michroma", "Arimo", sans-serif;
    font-size: 40px;
    color: var(--ghost);
    line-height: 1;
  }
  .capabilities-label {
    position: absolute;
    left: 22px;
    top: 316px;
    transform: rotate(-90deg);
    transform-origin: left top;
    display: flex;
    align-items: center;
    gap: 6px;
    font-size: 13px;
    font-weight: 700;
    letter-spacing: 0.5px;
    color: var(--ink-soft);
    white-space: nowrap;
  }
  .capabilities-label__arrow {
    width: 0; height: 0;
    border-top: 7px solid transparent;
    border-bottom: 7px solid transparent;
    border-left: 11px solid var(--accent);
    transform: rotate(90deg);
  }
  .capability-lines { position: absolute; left: 63px; top: 97px; width: 556px; list-style: none; }
  .capability-lines li {
    height: 38.5px;
    border-top: 2px dotted var(--rule);
  }
</style>
</head>
<body>

  <section class="card card--front" aria-label="Card front">
    <div class="brand">BRIGHTKEEL</div>
    <div class="brand__square" aria-hidden="true"></div>

    <div class="holder">
      <p class="holder__name">Firstname Surname</p>
      <p class="holder__role">Designation</p>
    </div>

    <div class="contact-panel" aria-hidden="true"></div>
    <ul class="contact">
      <li>M: 9999 999 999</li>
      <li>T: 99 9999 9999</li>
      <li>E: nnnn@nnn.com.au</li>
      <li>PO Box 99 Nnnnnnnnnn, Nnn, 9999</li>
      <li>ABN99999999999</li>
    </ul>
  </section>

  <section class="card card--back" aria-label="Card back">
    <div class="back-panel" aria-hidden="true"></div>
    <div class="ghost-brand" aria-hidden="true">BRIGHTKEEL</div>

    <div class="capabilities-label">
      <span class="capabilities-label__arrow" aria-hidden="true"></span>
      <span>COMPANY CAPABILTIES</span>
    </div>

    <ul class="capability-lines" aria-label="Capability notes">
      <li></li><li></li><li></li><li></li><li></li><li></li><li></li><li></li>
    </ul>
  </section>

</body>
</html>
```